Hvac and insulation company needs good looking business card design

We are hvac and insulation company and looking for a new business cards that look to today standards designs

Target Market(s)

homeowners

Industry/Entity Type

Hvac

Contact Information for Business Card

Name: Walter Brindley
Home comfort consultant
address: 4827 Moravia Ct #215 Oakland, CA 94602
office: 888-731-5096
cell: 510-842-3917
Lic.# 583164
Email: walter@corvane-hvac.example
Web: corvane-hvac.example

Requirements
Must have
• clean and sleek look
Nice to have
• simple with a clean look
Should not have
• to busy business card

```html
<!DOCTYPE html>
<html lang="en">
<head>
<meta charset="utf-8">
<title>Corvane Home Solutions – Business Card</title>
<link rel="stylesheet" href="https://fonts.googleapis.com/css2?family=Open+Sans:wght@400;600&family=Roboto+Condensed:wght@400;700&display=swap">
<style>
  :root {
    --orange: #f58a1f;
    --orange-light: #f9a03c;
    --white: #ffffff;
    --paper: #f1f1f1;
    --stripe: #9a9a9a;
    --page: #e6e6e6;
    --grey-text: #9b9b9b;
  }
  html, body {
    margin: 0;
    width: 1200px;
    height: 886px;
    overflow: hidden;
    background: var(--page);
  }
  .card {
    position: absolute;
    left: 330px;
    width: 540px;
    height: 309px;
    border-radius: 18px;
    overflow: hidden;
    box-shadow: 0 6px 18px rgba(0,0,0,.18);
  }
  .card-front { top: 100px; background: var(--orange); }
  .card-back { top: 477px; background: var(--paper); }
  .card-shapes { position: absolute; inset: 0; }

  .front-brand {
    position: absolute;
    right: 34px;
    bottom: 40px;
    text-align: left;
    color: var(--white);
    font-family: "Open Sans", sans-serif;
  }
  .front-brand .brand-name { font-size: 62px; font-weight: 600; line-height: 0.9; letter-spacing: -1px; }
  .front-brand .brand-tagline { font-size: 17px; letter-spacing: 3px; margin-left: 26px; }
  .front-brand .brand-web { font-size: 11px; letter-spacing: 5px; margin-left: 26px; margin-top: 4px; }

  .back-logo {
    position: absolute;
    left: 38px;
    top: 112px;
    display: flex;
    align-items: center;
    gap: 12px;
    font-family: "Open Sans", sans-serif;
  }
  .back-logo .logo-dot { width: 46px; height: 46px; border-radius: 50%; background: var(--orange); }
  .back-logo .brand-name { color: var(--orange); font-size: 44px; font-weight: 600; line-height: 0.9; letter-spacing: -1px; }
  .back-logo .brand-tagline { color: var(--grey-text); font-size: 13px; letter-spacing: 3px; margin-left: 4px; }

  .contact {
    position: absolute;
    right: 26px;
    top: 28px;
    text-align: right;
    color: var(--white);
    font-family: "Roboto Condensed", sans-serif;
  }
  .contact .person-name { font-size: 20px; font-weight: 700; text-transform: uppercase; }
  .contact .person-title { font-size: 14px; text-transform: uppercase; margin-bottom: 62px; }
  .contact-list { list-style: none; margin: 0; padding: 0; font-size: 14px; line-height: 19px; }
  .contact-list li { display: flex; justify-content: flex-end; align-items: center; gap: 6px; }
  .contact-list svg { width: 12px; height: 12px; flex: none; }
  .contact-list .no-icon { padding-right: 18px; }
</style>
</head>
<body>

<section class="card card-front">
  <svg class="card-shapes" viewBox="0 0 540 309" preserveAspectRatio="none">
    <polygon points="0,92 168,92 250,200 292,309 0,309" fill="var(--white)"/>
  </svg>
  <div class="front-brand">
    <div class="brand-name">corvane</div>
    <div class="brand-tagline">home solutions</div>
    <div class="brand-web">corvane-hvac.example</div>
  </div>
</section>

<section class="card card-back">
  <svg class="card-shapes" viewBox="0 0 540 309" preserveAspectRatio="none">
    <defs>
      <linearGradient id="orangeFade" x1="0" y1="0" x2="1" y2="1">
        <stop offset="0" stop-color="var(--orange)"/>
        <stop offset="1" stop-color="var(--orange-light)"/>
      </linearGradient>
    </defs>
    <polygon points="296,0 306,0 292,309 282,309" fill="var(--stripe)"/>
    <polygon points="306,0 540,0 540,309 292,309" fill="url(#orangeFade)"/>
  </svg>

  <div class="back-logo">
    <span class="logo-dot"></span>
    <div>
      <div class="brand-name">corvane</div>
      <div class="brand-tagline">home solutions</div>
    </div>
  </div>

  <div class="contact">
    <div class="person-name">Walter Brindley</div>
    <div class="person-title">CEO/Founder</div>
    <ul class="contact-list">
      <li class="no-icon">4827 Moravia Ct #215</li>
      <li class="no-icon">Oakland, CA 94602</li>
      <li>888-731-5096
        <svg viewBox="0 0 12 12"><path d="M2 1l2 0 1 3-1.3 1a6 6 0 0 0 3.3 3.3L8 7l3 1v2a1 1 0 0 1-1 1A9 9 0 0 1 1 2a1 1 0 0 1 1-1z" fill="var(--white)"/></svg></li>
      <li>510-842-3917
        <svg viewBox="0 0 12 12"><rect x="3" y="0.5" width="6" height="11" rx="1" fill="none" stroke="var(--white)"/><circle cx="6" cy="9.5" r=".8" fill="var(--white)"/></svg></li>
      <li>Lic.# 583164
        <svg viewBox="0 0 12 12"><rect x="1" y="3" width="10" height="7" rx="1" fill="var(--white)"/></svg></li>
      <li>walter@corvane-hvac.example
        <svg viewBox="0 0 12 12"><rect x="1" y="2.5" width="10" height="7" fill="var(--white)"/><path d="M1 2.5l5 4 5-4" fill="none" stroke="var(--orange)"/></svg></li>
      <li>corvane-hvac.example
        <svg viewBox="0 0 12 12"><circle cx="6" cy="6" r="5" fill="none" stroke="var(--white)"/><path d="M1 6h10M6 1c-3 3-3 7 0 10M6 1c3 3 3 7 0 10" fill="none" stroke="var(--white)" stroke-width=".8"/></svg></li>
    </ul>
  </div>
</section>

</body>
</html>
```